Deliver a professional and engaging investment propsal.

I am appealing to highend smart investors and need a high quality, engaging and formal presentation in PDF.
DropBox: https://www.filemarsh.net/sh/q8wz3kdmv2tanp7/BCxRp4LfWmZq9TnYeJ2sKo7vH?dl=0
Text for project is in Dropbox called New Proposal Final
Along with past much older attempts of this job.
Any additional ideas to enable a better outcome would be appreicated.

```html
<!DOCTYPE html>
<html lang="en">
<head>
<meta charset="utf-8">
<title>Prairie Line Business Park – Project Proposal</title>
<link rel="stylesheet" href="https://fonts.googleapis.com/css2?family=Source+Sans+3:wght@400;600;700;800&family=Arimo:wght@400;700&display=swap">
<style>
:root{
  --stage:#1c1c1e;
  --paper:#ffffff;
  --navy:#1d4f9c;
  --title-blue:#215aa5;
  --sky:#a9dcf2;
  --sky-soft:#d6eef9;
  --orange:#f0922b;
  --ink:#2b2b2b;
  --alert:#d8202a;
  --link:#1f3fb0;
}
*{box-sizing:border-box;margin:0;padding:0}
html,body{width:1029px;height:1200px;overflow:hidden;background:var(--stage)}
.canvas{position:relative;width:1029px;height:1200px}
.page{position:absolute;width:361px;height:511px;background:var(--paper);overflow:hidden;font-family:"Arimo",Arial,sans-serif;color:var(--ink)}
.p1{left:141px;top:77px}.p2{left:527px;top:77px}.p3{left:141px;top:613px}.p4{left:527px;top:613px}
.curve{position:absolute;inset:0;width:361px;height:511px}
.footer{position:absolute;left:0;bottom:0;width:361px;height:17px;background:var(--navy)}
.footer .tab{position:absolute;left:222px;top:0;width:88px;height:17px;background:var(--orange);clip-path:polygon(8px 0,100% 0,calc(100% - 8px) 100%,0 100%);color:#fff;font:700 5.5px/17px "Source Sans 3",sans-serif;text-align:center;letter-spacing:.2px}
.footer .num{position:absolute;right:18px;top:0;color:#fff;font:700 5.5px/17px "Source Sans 3",sans-serif}
.page-title{position:absolute;left:33px;top:33px;font:400 20px/1.05 "Source Sans 3",sans-serif;color:#333}
.title-rule{position:absolute;left:0;height:2px;background:var(--navy)}
.body{position:absolute;font-size:4.9px;line-height:1.32}
.body p{margin-bottom:5px}
.bullets{list-style:none}
.bullets li{position:relative;padding-left:8px;margin-bottom:3.5px}
.bullets li::before{content:"";position:absolute;left:1px;top:1.6px;width:2.4px;height:2.4px;border-radius:50%;background:var(--ink)}
.hl{color:var(--alert);font-weight:700}
.label{font-weight:700;margin-bottom:3px}
.media{position:absolute}
a{color:var(--link)}
/* cover */
.cover-photo{position:absolute;left:0;top:0;width:361px;height:360px;background:linear-gradient(180deg,#3c6ea8 0%,#7fa6cf 38%,#b2897a 62%,#6b5e58 80%,#8e8c8a 100%)}
.cover-kicker{position:absolute;left:33px;top:24px;font:800 16px/1 "Source Sans 3",sans-serif;color:#fff;letter-spacing:.3px}
.cover-title{position:absolute;left:33px;top:330px;font:800 25px/1.02 "Source Sans 3",sans-serif;color:var(--title-blue)}
.cover-sub{position:absolute;left:33px;top:383px;font:400 21px/1.05 "Source Sans 3",sans-serif;color:var(--orange)}
.cover-author{position:absolute;left:35px;top:476px;font:700 8px/1 "Source Sans 3",sans-serif;color:#222}
</style>
</head>
<body>
<div class="canvas">

<!-- Cover -->
<section class="page p1">
  <div class="cover-photo" role="img" aria-label="Photo of a modern four-storey hotel with brick and white facade at dusk"></div>
  <svg class="curve" viewBox="0 0 361 511" aria-hidden="true">
    <path d="M300,0 C330,120 300,250 361,330 L361,0Z" fill="var(--sky)" opacity=".55"/>
    <path d="M0,345 C140,300 260,320 361,250 L361,511 L0,511Z" fill="var(--paper)"/>
    <path d="M300,300 C330,380 300,450 340,511 L361,511 L361,245 Z" fill="var(--sky)"/>
  </svg>
  <div class="cover-kicker">PROJECT<br>PROPOSAL</div>
  <div class="cover-title">PRAIRIE LINE<br>BUSINESS PARK</div>
  <div class="cover-sub">60 ACRE MIXED-USE<br>DEVELOPMENT</div>
  <div class="cover-author">Daniel Harrow</div>
  <div class="footer"><div class="tab" style="left:222px;width:80px"></div></div>
</section>

<!-- Proposal -->
<section class="page p2">
  <svg class="curve" viewBox="0 0 361 511" aria-hidden="true">
    <path d="M290,0 C330,140 280,330 335,511 L361,511 L361,0Z" fill="var(--sky)"/>
  </svg>
  <h2 class="page-title">Proposal</h2>
  <div class="title-rule" style="top:55px;width:100px"></div>
  <div class="body" style="left:33px;top:70px;width:258px">
    <p>We have an incredible property, Prairie Line Business Park, located at 1780 Prairie Route 40 McKenzie County, Watford City, North Dakota USA which we have fully funded with cash and now need a joint venture partner, buyer or lender to get this project to completion and producing a substantial profit we all can share.</p>
    <p>Our property is located on the best oil reserves in the world in North Dakota USA, with more oil than any other county in the Bakken Basin and with the lowest recoverable costs of $24 a barrel.</p>
    <p>We own the property and need a partner to develop the site and bring to the market at half the cost of competing business parks in the area.</p>
  </div>
  <div class="body" style="left:33px;top:163px;width:130px">
    <div class="label">Participation Options</div>
    <ul class="bullets">
      <li><span class="hl">A joint venture partner</span> would support all the costs developing the property without the upfront costs of the property purchase.</li>
      <li>All sales would be split to ensure both parties are paid out in such a way that both are paid out in full at the same time then a 50/50 profit share split on all remaining sales.</li>
      <li>Contract drawn up protecting and supporting both parties on agreed terms.</li>
      <li>As a potential joint venture partner, I would cover the full property (57.7 acres) cost as mentioned of $124,784 per acre (57.7 acres). ($7,200,000)</li>
      <li>Joint venture partner to supply the development costs estimated to be around $65,000 an acre estimated pending tender selection and additional refundable security bonds held with the Watford City on development works.</li>
    </ul>
  </div>
  <div class="body" style="left:180px;top:174px;width:118px">
    <ul class="bullets">
      <li>Development costs could be in up to three stages to lower outlay and limit exposure if so desired, however it will take longer to complete and bring to market.</li>
      <li><span class="hl">A buyer</span> can be fully supported by myself to oversee the full project and outcomes and support the budgets of construction and sales to get the highest returns for a small fee.</li>
      <li>To purchase the property, you would need to contact me directly and I can introduce you to our realtor who will discount his commission from 6% to 5% which is a significant saving.</li>
      <li><span class="hl">Financing</span> on excellent terms allowing 12 to 18 months for income streams and could be linked to a joint venture option / profit share.</li>
    </ul>
  </div>
  <div class="body" style="left:33px;top:345px;width:200px;text-align:center;font-size:5px">
    <div style="font-weight:700">PRAIRIE LINE BUSINESS PARK</div>
    <div>60 ACRE MIXED-USE DEVELOPMENT</div>
  </div>
  <div class="media" style="left:35px;top:362px;width:199px;height:120px;background:linear-gradient(135deg,#b9c3a6,#d9dcd3 50%,#a8b893)" role="img" aria-label="Site plan of the 60 acre mixed-use development with lots marked sold"></div>
  <div class="media" style="left:239px;top:362px;width:96px;height:56px;background:linear-gradient(180deg,#8fb3d6,#9a5a45 55%,#6e5448)" role="img" aria-label="Rendering of a brick retail building"></div>
  <div class="media" style="left:239px;top:422px;width:96px;height:60px;background:linear-gradient(180deg,#b9cfe3,#d7c6ae 55%,#a48a72)" role="img" aria-label="Rendering of a hotel building marked coming soon"></div>
  <div class="footer"><div class="tab">PROJECT PROPOSAL</div><div class="num">02</div></div>
</section>

<!-- Major Site Changes -->
<section class="page p3">
  <svg class="curve" viewBox="0 0 361 511" aria-hidden="true">
    <path d="M300,0 C340,140 290,300 361,420 L361,0Z" fill="var(--sky)"/>
  </svg>
  <h2 class="page-title" style="top:32px">Major Site<br>Changes</h2>
  <div class="title-rule" style="top:76px;width:112px"></div>
  <div class="body" style="left:33px;top:98px;width:250px">
    <ul class="bullets">
      <li>We purchased the property in in 2013 for cash and without any additional debt, at the time we had highway 85 frontage just outside Watford City limits South of town with a zoning of agricultural within McKenzie County.</li>
      <li>2014 site zoning changed allowing a commercial zoning.</li>
      <li>Branded Hotel site purchased 2014 now with the option to purchase the franchise license and build the hotel ourselves.</li>
      <li>In 2016 we were added into City Limits which was a massive improvement to our site now taking advantage of confirmed city water and sewer was a great outcome.</li>
      <li>In 2016 the new bypass opened intersecting our highway frontage just 100 yards away which brings all the traffic in the Bakken right past our site which was a massive win for this project.</li>
      <li>Same commercial property listed across the road at $750,000 per acre retail at Ridgefield Commons and other business parks average listings $550,00 per acre.</li>
      <li>In late 2017 we applied for full site development application and were approved in mid-2018 which again was a significant improvement to the project.</li>
      <li>May 2018 Full site infrastructure development approval which includes all roads and city services, this will trigger interest in the site from passing traffic and with a great marketing campaign will surely start sales coming in quickly once we break ground and start work.</li>
      <li>We also can buy the franchise license of the Harbor Crest hotel for additional income potential if desired.</li>
    </ul>
  </div>
  <svg class="curve" viewBox="0 0 361 511" aria-hidden="true">
    <circle cx="335" cy="130" r="38" fill="none" stroke="#fff" stroke-width="3" stroke-dasharray="4 4"/>
    <circle cx="335" cy="130" r="35" fill="#b77a4d"/>
    <circle cx="335" cy="208" r="38" fill="none" stroke="#fff" stroke-width="3" stroke-dasharray="4 4"/>
    <circle cx="335" cy="208" r="35" fill="#9aa6a8"/>
  </svg>
  <div class="media" style="left:300px;top:95px;width:61px;height:70px" role="img" aria-label="Photo of an oil pump jack at sunset"></div>
  <div class="media" style="left:300px;top:173px;width:61px;height:70px" role="img" aria-label="Photo of a highway through open prairie"></div>
  <div class="media" style="left:0;top:280px;width:361px;height:214px;background:linear-gradient(180deg,#e8ecef 0%,#b9b4ab 30%,#8d8176 70%,#9c8a78 100%)" role="img" aria-label="Aerial photo of the development site outlined beside the highway"></div>
  <div class="body" style="left:88px;top:400px;width:150px;background:#fff;padding:2px;text-align:center;font-size:3.8px;line-height:1.25">60 acre development site. 2.7 acre sold already to the hotel brand going vertical this year. Development grows to $180,000 an acre with all city services on our front doorstep. Now with a new bypass past our site.</div>
  <div class="body" style="left:300px;top:418px;width:55px;color:#fff;font-size:3.8px;line-height:1.25">This property is currently listed for $175,000 an acre directly across the road.</div>
  <div class="footer"><div class="tab">PROJECT PROPOSAL</div><div class="num">03</div></div>
</section>

<!-- Location -->
<section class="page p4">
  <svg class="curve" viewBox="0 0 361 511" aria-hidden="true">
    <path d="M300,0 C330,110 300,230 361,330 L361,0Z" fill="var(--sky)"/>
  </svg>
  <h2 class="page-title">Location</h2>
  <div class="title-rule" style="top:55px;width:112px"></div>
  <div class="body" style="left:33px;top:70px;width:258px">
    <p>Our property is ideally located in Watford City, United States of America, despite its humble beginnings, has suddenly found itself at the epicentre of the Bakken oil boom Located in Western North Dakota the city has seen workers flood into the area over recent years to fill positions to support the growth.</p>
  </div>
  <div class="body" style="left:33px;top:109px;width:133px">
    <p>McKenzie County where Watford City is located has more recoverable oil and gas at the lowest recoverable cost per barrel at $24, making it most affordable anywhere in the Bakken basin, centrally located and very desirable area to establish a business and company headquarters.</p>
    <p>Watford City is the crossroads whereby around 20,000 vehicles pass by our site each day travelling locally and between Williston where boom started and Dickinson an established town with relevant established support for business and infrastructure. Our project has highway frontage and is 100 yards away from the bypass intersection making it the best location in McKenzie County for this type of project.</p>
    <p>With billions invested into infrastructure in the past 5 years in and around Bakken Shale Oil Basin our project has become the beneficiary of a major new Watford City bypass which intersects highway 85 just 100 yards south of our project, putting us on one of the busiest intersections in the Bakken. With this rapid growth we were included into the Watford City limits providing additional benefits to the overall success for our development including all city services.</p>
    <p>Demand stems from the ongoing boom in oil and gas drilling in the area which is still in its infancy stages of life, North Dakota oil play and is expected to continue to grow well past 2050 based on obtainable reserves beneath the ground.</p>
    <p style="margin-bottom:2px">Additional location growth:</p>
    <p style="margin-bottom:0"><a>Northgate Energy 150 million-dollar Watford City investment 2018</a><br><a>North Dakota is the nations second-biggest oil producer</a><br><a>McKenzie County Investment, Development</a></p>
  </div>
  <div class="body" style="left:180px;top:109px;width:120px">
    <p>Within the 100 yards of Prairie Line Business park, directly across the road commercial land is currently listed at of $750,000 an acre at Ridgefield Commons and many more locations up to $650,000 per acre. With an advantage over other sites in terms of a better location and much lower purchase and development costs the numbers don't lie, and we need to have pad ready to build lots to offer the market.</p>
    <p>Bakken traffic, North, South, East and West will have to travel right by our site making it the second busiest intersection in the Bakken area, giving us the best exposure to sell, promote and grow, this site can and will be the location for new business and growth, we need to develop the site now to move forward.</p>
    <p>With our obvious high exposure to potential buyers through the passing traffic and lower entry price point there is no doubt Prairie Line Town Center will become the place where business will want to build alongside a quality business like the Harbor Crest Suites Extended Stay Hotel.</p>
  </div>
  <div class="media" style="left:180px;top:360px;width:181px;height:105px;background:radial-gradient(ellipse at 55% 40%,#e9773a 0%,#f2c04e 38%,#e9dcae 70%,#cfd3cf 100%)" role="img" aria-label="Map of the Bakken oil patch counties in North Dakota"></div>
  <div class="body" style="left:180px;top:467px;width:181px;display:flex;gap:3px;font-size:2.8px;line-height:1.2">
    <div style="flex:1"><b>Oil basin</b><br>Main drilling zone in the west</div>
    <div style="flex:1"><b>Williston</b><br>Where the boom first started</div>
    <div style="flex:1"><b>Watford City</b><br>Central hub for new growth</div>
    <div style="flex:1"><b>Dickinson</b><br>Established support town</div>
    <div style="flex:1"><b>Minot</b><br>Regional air and rail link</div>
    <div style="flex:1"><b>Bismarck</b><br>State capital to the east</div>
  </div>
  <div class="footer"><div class="tab">PROJECT PROPOSAL</div><div class="num">04</div></div>
</section>

</div>
</body>
</html>
```